Film Company needs Poster Design Project for upcoming film "VANE"

At Brindlewood Films, we need a poster design for our upcoming feature film project "VANE," America first 'rock and roll' star. Our film will cover Tobias Merrick Vane's life his drinking, passion and writing. It will not be a horror film, but rather a biopic on his life.
Brindlewood Films is a full service film and television production company, founded by Curtis Belmont and Quarnet, LLC in 2006. Brindlewood Films’ mission is to blend artistic talent with engaging stories to create feature films and television that delight audiences of all ages.
We would like to see designs that embody Tobias Merrick Vane as a person. The film will cover most of his famous poems/novels/short stories so any reference to "Hollow lantern" or "The Quill Moth," etc...would work.
Updates
Thank you ALL for the amazing work you have submitted, you made it really hard for me to come up with one choice. I will make my decision by Wednesday.
Target Market(s)
Target audience 18 - 35
Industry/Entity Type
It Company
Look and feel

```html
<!DOCTYPE html>
<html lang="en">
<head>
<meta charset="utf-8">
<title>VANE – Brindlewood Films poster</title>
<link rel="stylesheet" href="https://fonts.googleapis.com/css2?family=Antonio:wght@100;200;300&family=Roboto+Condensed:wght@300&display=swap">
<style>
  :root {
    --page: #ffffff;
    --ink: #1e1c1c;
    --blue: #0a7cc4;
    --bar-text: #e9f3fb;
    --sky-light: #ffffff;
    --sky-mid: #e6e6e6;
    --sky-edge: #c9c9c9;
    --ground: #1f1d1d;
    --caption: #7b7b7b;
  }
  html, body {
    margin: 0;
    padding: 0;
    width: 1200px;
    height: 1000px;
    overflow: hidden;
    background: var(--page);
  }
  .canvas {
    position: relative;
    width: 1200px;
    height: 1000px;
  }
  .poster {
    position: absolute;
    left: 63px;
    top: 0;
    width: 750px;
    height: 1000px;
    overflow: hidden;
    background: radial-gradient(ellipse 75% 60% at 50% 72%, var(--sky-light) 0%, var(--sky-mid) 55%, var(--sky-edge) 100%);
  }
  .tagline-bar {
    position: absolute;
    left: 0;
    top: 22px;
    width: 100%;
    height: 36px;
    background: var(--blue);
    color: var(--bar-text);
    font-family: "Antonio", sans-serif;
    font-weight: 200;
    font-size: 28px;
    line-height: 36px;
    letter-spacing: 8px;
    text-align: center;
    text-transform: uppercase;
  }
  .studio {
    position: absolute;
    left: 0;
    top: 160px;
    width: 100%;
    margin: 0;
    text-align: center;
    color: var(--ink);
    font-family: "Antonio", sans-serif;
    font-weight: 200;
    font-size: 32px;
    line-height: 36px;
    letter-spacing: 9px;
    text-transform: uppercase;
  }
  .presents {
    position: absolute;
    left: 0;
    top: 208px;
    width: 100%;
    margin: 0;
    text-align: center;
    color: var(--ink);
    font-family: "Antonio", sans-serif;
    font-weight: 200;
    font-size: 22px;
    line-height: 26px;
    letter-spacing: 20px;
    padding-left: 20px;
    box-sizing: border-box;
    text-transform: uppercase;
  }
  .film-title {
    position: absolute;
    left: 0;
    top: 232px;
    width: 100%;
    margin: 0;
    text-align: center;
    color: var(--ink);
    font-family: "Antonio", sans-serif;
    font-weight: 300;
    font-size: 300px;
    line-height: 270px;
    letter-spacing: 6px;
  }
  .burial-scene {
    position: absolute;
    left: 0;
    top: 630px;
    width: 100%;
    height: 370px;
    background:
      radial-gradient(ellipse 48% 30% at 45% 62%, rgba(10, 124, 196, 0.55) 0%, rgba(10, 124, 196, 0) 100%),
      linear-gradient(to bottom, rgba(31, 29, 29, 0) 0px, rgba(31, 29, 29, 0.85) 30px, var(--ground) 38px, var(--ground) 100%);
  }
  .caption {
    position: absolute;
    left: 970px;
    top: 638px;
    width: 220px;
    margin: 0;
    color: var(--caption);
    font-family: "Roboto Condensed", sans-serif;
    font-weight: 300;
    font-size: 25px;
    line-height: 50.5px;
  }
</style>
</head>
<body>
  <main class="canvas">
    <section class="poster">
      <div class="tagline-bar">America’s first ‘rock and roll’ star</div>
      <p class="studio">Brindlewood Films</p>
      <p class="presents">Present</p>
      <h1 class="film-title">VANE</h1>
      <div class="burial-scene" role="img" aria-label="Illustration of grass at ground level above dark earth, with a blue silhouette of Tobias Merrick Vane lying buried beneath"></div>
    </section>
    <p class="caption">Inspired by<br>Vane’s morbid<br>obsession/ fear of<br>being buried alive,<br>as extrapolated<br>in his story ‘The<br>Shallow Vault’.</p>
  </main>
</body>
</html>
```